Male Chastity Keyholding Service Image

NOTE: ADULT ORIENTED PROJECTI am looking for a design that better communicates the service we offer in a more stylish approach. I have attached the current image we are utilizing for this Keyholding Service. The service we offer is we will ship the customer a padlock immediately with their order, then, based on the length of time the customer selected (1-6 weeks), we will ship the keys to them at a later time.The purpose of this service is to give customers whom do not have a partner to play the male chastity game with them an opportunity to experience real chastity without access to their keys.

Target Market(s)

Adult

Requirements
Nice to have
• Color Code - #8410ea
• This color is is our signature purple

```html
<!DOCTYPE html>
<html lang="en">
<head>
<meta charset="utf-8">
<title>Male Chastity Keyholding Service</title>
<link rel="stylesheet" href="https://fonts.googleapis.com/css2?family=Montserrat:wght@600;800&family=Questrial&family=Roboto:wght@400&display=swap">
<style>
  :root {
    --purple: #8410ea;
    --paper: #fafafa;
    --ink: #1f1f1f;
    --slate: #3d4144;
    --stage: #000000;
    --white: #ffffff;
  }
  * { margin: 0; padding: 0; box-sizing: border-box; }
  html, body {
    width: 1200px; height: 905px; overflow: hidden;
    background: var(--stage);
  }
  .canvas { position: relative; width: 1200px; height: 905px; }
  .flyer {
    position: absolute; left: 389px; top: 154px;
    width: 422px; height: 596px;
    background: var(--paper);
    overflow: hidden;
  }
  .masthead {
    height: 93px; background: var(--purple); color: var(--white);
    text-align: center; padding-top: 18px;
  }
  .masthead__title {
    font-family: "Montserrat", sans-serif; font-weight: 600;
    font-size: 32px; line-height: 34px; letter-spacing: -0.5px;
  }
  .masthead__subtitle {
    font-family: "Questrial", sans-serif; font-weight: 700;
    font-size: 24px; line-height: 24px; letter-spacing: 1.8px;
    -webkit-text-stroke: 0.6px var(--white);
  }
  .headline {
    height: 146px; text-align: center; padding-top: 36px;
  }
  .headline__main {
    font-family: "Montserrat", sans-serif; font-weight: 800;
    font-size: 50px; line-height: 54px; color: var(--purple);
  }
  .headline__sub {
    font-family: "Montserrat", sans-serif; font-weight: 800;
    font-size: 26px; line-height: 30px; color: var(--slate); letter-spacing: 0.5px;
  }
  .icon-band { height: 214px; background: var(--purple); position: relative; }
  .icon-band svg { position: absolute; left: 0; top: 0; }
  .pitch {
    text-align: center; padding-top: 32px;
    font-family: "Roboto", sans-serif; font-size: 14px; line-height: 17px;
    color: var(--ink);
  }
  .pitch__tag {
    display: inline-block; margin-top: 10px;
    width: 130px; height: 33px; border: 2.5px solid var(--purple);
    border-radius: 17px; color: var(--purple);
    font-family: "Questrial", sans-serif; font-size: 21px; line-height: 28px;
    letter-spacing: 1px;
  }
  .footer-wedge { position: absolute; left: 0; bottom: 0; }
</style>
</head>
<body>
<div class="canvas">
  <article class="flyer">
    <header class="masthead">
      <h1 class="masthead__title">MALE CHASTITY</h1>
      <p class="masthead__subtitle">Keyholding Service</p>
    </header>
    <section class="headline">
      <h2 class="headline__main">PADLOCK</h2>
      <p class="headline__sub">IMMEDIATELY</p>
    </section>
    <section class="icon-band">
      <svg width="422" height="214" viewBox="0 0 422 214" aria-label="Open padlock and a set of keys">
        <g class="icon-padlock" fill="none" stroke="var(--white)" stroke-width="8" stroke-linejoin="round">
          <path d="M74 98 V57 a26 26 0 0 1 52 0 V104" stroke-linecap="round"/>
          <path d="M100 104 H192 V170 Q146 174 100 170 Z"/>
          <circle cx="71" cy="91" r="4" fill="var(--white)" stroke="none"/>
        </g>
        <g class="icon-keys" fill="var(--white)">
          <circle cx="283" cy="44" r="18" fill="none" stroke="var(--white)" stroke-width="6"/>
          <g transform="rotate(-32 310 75)">
            <rect x="297" y="66" width="30" height="48" rx="13" fill="none" stroke="var(--white)" stroke-width="5"/>
            <path d="M303 78h18M303 86h18M303 94h18M303 102h18" stroke="var(--white)" stroke-width="3"/>
            <path d="M306 114h12v64l-6 6h-2v-8l4-3-4-3v-5l4-3-4-3z"/>
          </g>
          <rect x="266" y="62" width="36" height="54" rx="14" fill="none" stroke="var(--white)" stroke-width="5"/>
          <path d="M272 74h24M272 81h24M272 88h24M272 95h24M272 102h24" stroke="var(--white)" stroke-width="3"/>
          <path d="M277 116h14v74l-8 8h-2v-10l5-3-5-3v-6l5-3-5-3z"/>
        </g>
      </svg>
    </section>
    <section class="pitch">
      <p>Opportunity to experience real chastity<br>without access to their</p>
      <span class="pitch__tag">KEYS</span>
    </section>
    <svg class="footer-wedge" width="422" height="24" viewBox="0 0 422 24" aria-hidden="true">
      <polygon points="0,24 422,0 422,24" fill="var(--purple)"/>
    </svg>
  </article>
</div>
</body>
</html>
```